Business Card Design

Mortgage brokering company, also providing Commercial Finance, Car Finance and Insurance.

Target Market(s)

Home Buyers

Industry/Entity Type

Business

Contact Information for Business Card

All information required on business card is contained in the attachment. Design does not have to follow the style of the attachment.

```html
<!DOCTYPE html>
<html lang="en">
<head>
<meta charset="utf-8">
<title>Keystone Home Lending – Business Card</title>
<link rel="stylesheet" href="https://fonts.googleapis.com/css2?family=Open+Sans:wght@400;600&display=swap">
<style>
  :root {
    --stage: #2a2a2c;
    --card-dark: #121214;
    --card-mid: #34353a;
    --accent-red: #c4161c;
    --accent-red-dark: #8f0f13;
    --paper: #f1f1f1;
    --paper-shade: #d6d6d6;
    --ink: #3a3a3a;
    --tagline: #9a9a9e;
    --white: #ffffff;
    --logo-mark: #f29a1f;
  }
  * { box-sizing: border-box; margin: 0; padding: 0; }
  html, body { width: 1200px; height: 1000px; overflow: hidden; }
  body {
    background: var(--stage);
    font-family: "Open Sans", Arial, sans-serif;
    position: relative;
  }
  .card {
    position: absolute;
    left: 250px;
    width: 700px;
    height: 400px;
    overflow: hidden;
    border-radius: 3px;
    box-shadow: 0 12px 30px rgba(0,0,0,0.5);
  }
  .card--front { top: 55px; }
  .card--back { top: 545px; }

  /* textured dark field: texture and chevron decoration shown as a soft gradient */
  .card__texture {
    position: absolute; inset: 0;
    background:
      radial-gradient(ellipse 55% 70% at 48% 45%, var(--card-mid) 0%, rgba(52,53,58,0) 70%),
      linear-gradient(180deg, #1b1b1e 0%, var(--card-dark) 100%);
  }

  /* front */
  .front__rule {
    position: absolute; left: 0; right: 0; top: 262px;
    height: 3px; background: var(--accent-red);
  }
  .front__base {
    position: absolute; left: 0; right: 0; bottom: 0; height: 46px;
    background: linear-gradient(var(--paper), var(--paper-shade));
  }

  .brand {
    position: absolute;
    display: flex; align-items: flex-start; gap: 12px;
  }
  .brand__mark { background: var(--logo-mark); flex: none; }
  .brand__text { display: flex; flex-direction: column; align-items: flex-end; }
  .brand__name {
    color: var(--white); font-weight: 400; white-space: nowrap; line-height: 1.1;
  }
  .brand__tagline {
    color: var(--tagline); font-weight: 400; text-transform: uppercase;
    white-space: nowrap; line-height: 1;
  }

  .front__brand { left: 50%; top: 186px; transform: translateX(-50%); }
  .front__brand .brand__mark { width: 44px; height: 44px; margin-top: 2px; }
  .front__brand .brand__name { font-size: 30px; }
  .front__brand .brand__tagline { font-size: 11px; letter-spacing: 3px; margin-top: 2px; }

  /* back */
  .back__texture { bottom: 180px; }
  .back__brand { right: 40px; top: 62px; }
  .back__brand .brand__mark { width: 36px; height: 36px; margin-top: 2px; }
  .back__brand .brand__name { font-size: 24px; }
  .back__brand .brand__tagline { font-size: 10px; letter-spacing: 2.5px; margin-top: 2px; }

  .back__panel {
    position: absolute; left: 0; right: 0; bottom: 0; height: 180px;
    background: linear-gradient(var(--paper), var(--paper-shade));
    border-top: 3px solid var(--accent-red);
  }
  .name-tab {
    position: absolute; left: 0; top: 42px;
    width: 235px; height: 72px;
    background: linear-gradient(var(--accent-red), var(--accent-red-dark));
    border-radius: 0 10px 10px 0;
    color: var(--white); text-align: center;
    padding-top: 10px;
  }
  .name-tab__name { font-size: 26px; font-weight: 400; letter-spacing: 0.5px; line-height: 1.1; }
  .name-tab__role { font-size: 13px; font-weight: 400; }

  .contacts {
    position: absolute; left: 262px; top: 28px; right: 20px;
    color: var(--ink); font-size: 13px;
  }
  .contact { position: absolute; display: flex; align-items: center; gap: 8px; white-space: nowrap; }
  .contact__icon {
    width: 18px; height: 18px; border-radius: 50%;
    background: var(--ink); flex: none;
    display: flex; align-items: center; justify-content: center;
  }
  .contact__icon svg { width: 11px; height: 11px; fill: var(--white); }
  .contact--phone { left: 0; top: 0; }
  .contact--mobile { left: 0; top: 30px; }
  .contact--web { left: 215px; top: 0; }
  .contact--email { left: 215px; top: 30px; }
  .contact--address { left: 0; top: 60px; align-items: flex-start; }
  .contact__address { line-height: 1.35; }
  .contact__address strong { font-weight: 600; display: block; }
</style>
</head>
<body>

  <section class="card card--front" aria-label="Business card front">
    <div class="card__texture" role="img" aria-label="Dark carbon-fibre texture with large faint chevron shapes"></div>
    <div class="front__rule"></div>
    <div class="front__base"></div>
    <div class="brand front__brand">
      <span class="brand__mark"></span>
      <span class="brand__text">
        <span class="brand__name">Keystone Home Lending</span>
        <span class="brand__tagline">Consulting</span>
      </span>
    </div>
  </section>

  <section class="card card--back" aria-label="Business card back">
    <div class="card__texture back__texture" role="img" aria-label="Dark carbon-fibre texture with large faint chevron shapes"></div>
    <div class="brand back__brand">
      <span class="brand__mark"></span>
      <span class="brand__text">
        <span class="brand__name">Keystone Home Lending</span>
        <span class="brand__tagline">Consulting</span>
      </span>
    </div>

    <div class="back__panel">
      <div class="name-tab">
        <p class="name-tab__name">MARCUS HALE</p>
        <p class="name-tab__role">Credit Representative</p>
      </div>

      <div class="contacts">
        <div class="contact contact--phone">
          <span class="contact__icon"><svg viewBox="0 0 24 24"><path d="M6.6 10.8a15 15 0 0 0 6.6 6.6l2.2-2.2a1 1 0 0 1 1-.25 11.4 11.4 0 0 0 3.6.57 1 1 0 0 1 1 1V20a1 1 0 0 1-1 1A17 17 0 0 1 3 4a1 1 0 0 1 1-1h3.5a1 1 0 0 1 1 1c0 1.25.2 2.45.57 3.57a1 1 0 0 1-.25 1z"/></svg></span>
          <span>555 210 7788</span>
        </div>
        <div class="contact contact--mobile">
          <span class="contact__icon"><svg viewBox="0 0 24 24"><path d="M7 2h10a2 2 0 0 1 2 2v16a2 2 0 0 1-2 2H7a2 2 0 0 1-2-2V4a2 2 0 0 1 2-2zm0 3v12h10V5z"/></svg></span>
          <span>0412 880 316</span>
        </div>
        <div class="contact contact--web">
          <span class="contact__icon"><svg viewBox="0 0 24 24"><path d="M12 2a10 10 0 1 0 0 20 10 10 0 0 0 0-20zm0 2c1.2 1.4 2 3.5 2.2 6H9.8C10 7.5 10.8 5.4 12 4zm-2.2 8h4.4c-.2 2.5-1 4.6-2.2 6-1.2-1.4-2-3.5-2.2-6zM4.1 11a8 8 0 0 1 3.7-5.6C7.3 7 7 8.9 7.8 11zm0 2h3.7c.1 2 .5 3.9 1.2 5.4A8 8 0 0 1 4.1 13zm12.1 0h3.7a8 8 0 0 1-4.9 5.4c.7-1.5 1.1-3.4 1.2-5.4zm0-2c-.1-2-.5-3.9-1.2-5.4A8 8 0 0 1 19.9 11z"/></svg></span>
          <span>www.keystonehl.com</span>
        </div>
        <div class="contact contact--email">
          <span class="contact__icon"><svg viewBox="0 0 24 24"><path d="M3 5h18v14H3zm2 2v.5l7 4.5 7-4.5V7zm0 2.8V17h14V9.8l-7 4.5z"/></svg></span>
          <span>email</span>
        </div>
        <div class="contact contact--address">
          <span class="contact__icon"><svg viewBox="0 0 24 24"><path d="M12 2a7 7 0 0 0-7 7c0 5 7 13 7 13s7-8 7-13a7 7 0 0 0-7-7zm0 9.5A2.5 2.5 0 1 1 12 6.5a2.5 2.5 0 0 1 0 5z"/></svg></span>
          <span class="contact__address"><strong>Keystone Home Lending</strong>1180 Harbor Lane, Lakeview, State 60214</span>
        </div>
      </div>
    </div>
  </section>

</body>
</html>
```